Wix Website design for my therapy business - Willowmere Group

I have started designing a Wix site and have a good idea of what I want.
I have set up the pages, created some design ideas, and inputted the copy. I need someone fabulous to finish off the design aspects. I like working closely with the designers, I was an interior designer in an old career.
I would like the site to be funky but professional. My Wix skills are limited, and I just can't achieve the look I am wanting without having to spend a lot of time learning. If it's easier to start over, that's ok providing you use the same colours, font, images etc. I have included a screenshot of the home page below. I have another site I need to start as soon as we have finished this one.
I am looking for someone who is a good listener and is has design flare. I am easy to get along with and will respond quickly.
I would like to set up SEO and have help in the future.
Let me know if you are the right person for the job.
Target Market(s)
Please needing help with their mental health and for therapy.
Industry/Entity Type
Mental health
Font styles to use
Other font styles liked:
- Futura light
Requirements
Must have
- be easy to navigate and be simple yet stylish
Nice to have
- I have set up the basics of the site - nice to haves are already on the site
Should not have
- old fashioned large chunks of text.

```html
<!DOCTYPE html>
<html lang="en">
<head>
<meta charset="UTF-8">
<title>Willowmere Group — Improving care. Changing lives.</title>
<link href="https://fonts.googleapis.com/css2?family=Jost:wght@300;400;500;600;800&display=swap" rel="stylesheet">
<style>
:root{
  --brown:#9c7c62;
  --brown-dark:#7f624b;
  --forest:#1e2824;
  --peach:#efc9a2;
  --mist:#eef4f5;
  --ink:#1b1b1b;
  --muted:#444;
  --white:#ffffff;
  --grey-pill:#8a8f8c;
}
*{margin:0;padding:0;box-sizing:border-box}
html,body{width:1200px;height:4286px;overflow:hidden}
body{font-family:"Jost",sans-serif;color:var(--ink);background:var(--white);position:relative}
.abs{position:absolute}
section,header,footer{position:absolute;left:0;width:1200px;overflow:hidden}
p{font-weight:300;font-size:12.5px;line-height:21px}
.label{font-size:13px;font-weight:500;letter-spacing:.2px;text-transform:uppercase}
.rule{height:1px;background:#9a9a9a;position:absolute}
.btn{position:absolute;display:flex;align-items:center;gap:8px;height:28px;padding:0 18px;border-radius:14px;font-size:12px;font-weight:500;white-space:nowrap}
.btn svg{width:30px;height:8px}
.btn-white{background:var(--white);color:var(--ink)}
.btn-brown{background:var(--brown);color:var(--white)}
.link-arrow{position:absolute;display:flex;align-items:center;gap:8px;font-size:12px;font-weight:500}
.link-arrow svg{width:30px;height:8px}
.logo{font-family:"Jost",sans-serif;font-weight:500;font-size:24px;color:var(--brown);letter-spacing:-.3px;white-space:nowrap}
.photo{position:absolute}

/* header */
.site-header{top:0;height:75px;background:var(--white)}
.site-header .logo{position:absolute;left:111px;top:22px}
.nav{position:absolute;top:47px;left:321px;display:flex;gap:0;font-size:12.5px;font-weight:400;color:#333}
.nav a{color:inherit;text-decoration:none;margin-right:29px}
.nav a.active{color:var(--brown)}
.search{position:absolute;left:872px;top:11px;width:28px;height:28px;border:1px solid #444;border-radius:50%}
.appt{left:915px;top:10px;height:30px;width:172px;justify-content:center;font-size:12px}

/* hero */
.hero{top:75px;height:602px;background:linear-gradient(100deg,#3a2f25 0%,#6b5a44 35%,#b79a78 60%,#d8c2a4 80%,#8a7a5c 100%)}
.hero .eyebrow{position:absolute;left:111px;top:198px;color:var(--white);font-size:13px;font-weight:500}
.hero h1{position:absolute;left:111px;top:218px;color:var(--white);font-weight:800;font-size:50px;line-height:60px;letter-spacing:.5px}
.hero p{position:absolute;left:111px;top:351px;width:440px;color:var(--white);font-size:12px;line-height:20px}
.hero .btn{left:111px;top:424px}

/* programs */
.programs{top:677px;height:483px;background:var(--white)}
.programs .label{position:absolute;left:111px;top:73px;text-transform:none;font-size:13px}
.prog-card{position:absolute;left:111px;top:118px;width:550px;height:180px;background:var(--peach);border-radius:12px}
.prog-card h3{position:absolute;left:76px;top:22px;font-size:19px;font-weight:500}
.prog-card p{position:absolute;left:76px;top:56px;width:440px;font-size:11.5px;line-height:20px}
.prog-card .link-arrow{left:76px;top:135px}
.prog-item{position:absolute;left:141px;display:flex;align-items:center;gap:20px;font-size:19px;font-weight:500}
.prog-icon{position:absolute;width:24px;height:26px}

/* toolbox */
.toolbox{top:1160px;height:571px;background:var(--forest);color:var(--white)}
.pill{position:absolute;height:34px;border-radius:17px;background:var(--grey-pill);color:#e8e8e8;font-size:11.5px;display:flex;align-items:center;justify-content:center;letter-spacing:.2px}
.pill b{font-weight:400;color:#222}
.node{position:absolute;width:120px;height:120px;border-radius:50%;background:var(--white);color:#222;display:flex;flex-direction:column;align-items:center;justify-content:center;font-size:9.5px;text-align:center;line-height:11px;gap:4px}
.node.active{background:var(--brown);color:#eee;box-shadow:0 0 0 6px rgba(156,124,98,.35)}
.node svg.icon{width:30px;height:30px}
.node svg.arr{width:18px;height:6px}
.hub{position:absolute;left:281px;top:250px;width:144px;height:50px;border-radius:25px;background:var(--white);border:3px solid var(--brown);display:flex;align-items:center;justify-content:center;font-size:17px;font-weight:500;color:var(--brown)}
.toolbox .label{position:absolute;left:672px;top:151px;font-size:12.5px}
.toolbox .rule{left:672px;top:174px;width:416px;background:#777}
.toolbox h2{position:absolute;left:672px;top:182px;font-size:34px;font-weight:500;line-height:46px}
.toolbox p{position:absolute;left:672px;top:285px;width:380px;color:#ddd;font-size:12px}
.toolbox .btn{left:672px;top:388px}

/* find */
.find{top:1731px;height:590px;background:var(--mist)}
.find .panel{position:absolute;left:772px;top:0;width:428px;height:590px;background:var(--brown)}
.find .label{position:absolute;left:111px;top:54px;font-size:12.5px}
.find .rule{left:111px;top:76px;width:335px}
.find h2{position:absolute;left:111px;top:86px;font-size:35px;font-weight:400;line-height:45px}
.find p{position:absolute;left:111px;top:190px;width:470px;font-size:11.5px;line-height:20px}
.opt{position:absolute;display:flex;align-items:center;gap:12px;font-size:12px;color:#333}
.opt i{display:block;width:26px;height:26px;border-radius:50%;border:1px solid #888;background:var(--white)}
.find .btn{left:111px;top:422px;height:28px}

/* case */
.case-photo{top:2248px;left:0;width:428px;height:443px;background:linear-gradient(160deg,#e8e6e2,#c7bcae 55%,#8c7a69)}
.case{top:2321px;left:428px;width:772px;height:370px;background:var(--forest);color:var(--white)}
.case .label{position:absolute;left:36px;top:56px;font-size:12.5px}
.case .count{position:absolute;left:487px;top:57px;font-size:11px;font-weight:500}
.circ-btn{position:absolute;top:48px;width:32px;height:32px;border:1px solid #ddd;border-radius:50%;display:flex;align-items:center;justify-content:center}
.case h2{position:absolute;left:36px;top:94px;font-size:25px;font-weight:500}
.case p{position:absolute;left:36px;top:143px;width:490px;color:#ddd;font-size:11.8px}
.case .btn{left:38px;top:276px}

/* about */
.about{top:2691px;height:537px;background:var(--mist)}
.about .label{position:absolute;left:111px;top:158px;font-size:12.5px}
.about .rule{left:111px;top:180px;width:335px}
.about h2{position:absolute;left:111px;top:190px;font-size:35px;font-weight:400}
.about p{position:absolute;left:111px;top:254px;width:520px;font-size:11.5px;line-height:20px}
.about .btn{left:111px;top:354px}

/* insights */
.insight{height:341px}
.insight .label{position:absolute;font-size:12.5px}
.insight h2{position:absolute;font-size:26px;font-weight:400;line-height:32px}
.insight p{position:absolute;width:440px;font-size:11.8px;line-height:20.5px}
.ins-a{top:3228px;background:var(--forest);color:var(--white)}
.ins-b{top:3569px;background:var(--brown);color:var(--white)}

/* newsletter */
.newsletter{top:3910px;height:242px;background:var(--white);text-align:center}
.newsletter h2{position:absolute;left:0;width:1200px;top:60px;font-size:35px;font-weight:500}
.newsletter p{position:absolute;left:340px;width:520px;top:121px;font-size:11.8px}
.email{position:absolute;left:364px;top:182px;width:468px;height:42px;border:1px solid #bbb;border-radius:21px;text-align:left}
.email span{position:absolute;left:24px;top:12px;font-size:11.5px;color:#999;font-weight:300}
.email .btn{right:2px;top:2px;height:36px;border-radius:18px;width:136px;justify-content:center;gap:28px}

/* footer */
.site-footer{top:4152px;height:134px;background:var(--white)}
.site-footer .logo{position:absolute;left:111px;top:34px}
.foot-links{position:absolute;left:363px;top:40px;display:flex;gap:30px;font-size:12px;color:#333}
.social{position:absolute;top:32px;width:30px;height:30px;border:1.5px solid #222;border-radius:50%}
.site-footer .rule{left:111px;top:100px;width:977px;background:#ccc}
.copy{position:absolute;top:111px;font-size:11px;color:#333}
</style>
</head>
<body>

<header class="site-header">
  <div class="logo">Willowmere Group</div>
  <nav class="nav">
    <a class="active">Home</a><a>About Us</a><a>EMDR</a><a>Addiction</a><a>Betrayal Trauma</a><a>PTSD</a><a>Program List</a><a>Resources</a><a>Blog</a><a>Contact Us</a>
  </nav>
  <div class="search"><svg viewBox="0 0 28 28" width="28" height="28"><circle cx="13" cy="13" r="4.5" fill="none" stroke="#222" stroke-width="1.5"/><line x1="16.3" y1="16.3" x2="19" y2="19" stroke="#222" stroke-width="1.5"/></svg></div>
  <div class="btn btn-brown appt">Make an Appointment</div>
</header>

<section class="hero" role="img" aria-label="Photo of a smiling family playing outdoors at sunset">
  <div class="eyebrow">Welcome to The Willowmere Group</div>
  <h1>Improving care.<br>Changing lives.</h1>
  <p>Industry-leading evidence-based solutions that enable healthcare organizations to deliver care that leads to better lives for all.</p>
  <div class="btn btn-white">See Our Impact <svg viewBox="0 0 30 8"><path d="M0 4h28M24 1l4 3-4 3" fill="none" stroke="#222" stroke-width="1"/></svg></div>
</section>

<section class="programs">
  <div class="label">Our Programs</div>
  <div class="rule" style="left:111px;top:96px;width:335px"></div>
  <div class="prog-card">
    <svg class="prog-icon" style="left:22px;top:20px;width:34px;height:30px" viewBox="0 0 34 30"><path d="M17 28C7 20 3 15 3 9a6 6 0 0 1 14-3 6 6 0 0 1 14 3c0 6-4 11-14 19z" fill="#2a2a2a"/><circle cx="17" cy="14" r="3" fill="var(--peach)"/></svg>
    <h3>Children &amp; Families</h3>
    <p>Lorem ipsum dolor sit amet, consectetur adipiscing elit. Vestibulum posuere elementum purus ut hendrerit. Vestibulum in leo rutrum, suscipit massa sit amet, placerat metus. Nam vulputate eleifend maximus.</p>
    <div class="link-arrow">See Our Impact <svg viewBox="0 0 30 8"><path d="M0 4h28M24 1l4 3-4 3" fill="none" stroke="#222" stroke-width="1"/></svg></div>
  </div>
  <svg class="prog-icon" style="left:141px;top:330px" viewBox="0 0 24 26"><rect x="3" y="1" width="14" height="20" rx="1" fill="none" stroke="#2a2a2a" stroke-width="2"/><path d="M6 6h8M6 10h8M6 14h5" stroke="#2a2a2a" stroke-width="1.5"/><circle cx="18" cy="20" r="5" fill="#2a2a2a"/></svg>
  <div class="prog-item" style="left:187px;top:329px">Change Makers</div>
  <svg class="prog-icon" style="left:141px;top:390px" viewBox="0 0 24 26"><rect x="1" y="2" width="14" height="12" rx="1" fill="none" stroke="#2a2a2a" stroke-width="2"/><circle cx="15" cy="16" r="6" fill="none" stroke="#2a2a2a" stroke-width="2"/><path d="M19 20l4 4" stroke="#2a2a2a" stroke-width="2"/></svg>
  <div class="prog-item" style="left:187px;top:389px">Professionals</div>
  <div class="photo" role="img" aria-label="Circular photo of a family lying head to head on the grass" style="left:758px;top:92px;width:320px;height:320px;border-radius:50%;background:radial-gradient(circle at 50% 45%,#d8b49a,#8d7b6a 60%,#556348)"></div>
</section>

<section class="toolbox">
  <div class="pill" style="left:160px;top:45px;width:407px">SOLUTIONS<b>&nbsp;THAT BENEFIT MEDICAL TEAMS</b></div>
  <svg class="abs" style="left:0;top:0" width="720" height="571" viewBox="0 0 720 571">
    <g fill="none" stroke="#d9d9d9" stroke-width="6" stroke-dasharray="2 3">
      <path d="M175 226C190 270 230 270 281 275"/>
      <path d="M353 226V250"/>
      <path d="M531 226C516 270 476 270 425 275"/>
      <path d="M175 323C190 285 230 280 281 280"/>
      <path d="M353 300V323"/>
      <path d="M531 323C516 285 476 280 425 280"/>
    </g>
  </svg>
  <div class="node active" style="left:115px;top:106px">
    <svg class="icon" viewBox="0 0 30 30"><rect x="6" y="3" width="18" height="24" rx="1" fill="none" stroke="#eee" stroke-width="1.5"/><path d="M10 9h10M10 13h10M10 17h10M10 21h6" stroke="#eee" stroke-width="1.3"/></svg>
    Knowledge<br>Analyzer
    <svg class="arr" viewBox="0 0 18 6"><path d="M0 3h16M13 1l3 2-3 2" fill="none" stroke="#eee"/></svg>
  </div>
  <div class="node" style="left:293px;top:106px">
    <svg class="icon" viewBox="0 0 30 30"><rect x="6" y="3" width="18" height="24" rx="1" fill="none" stroke="#222" stroke-width="1.5"/><path d="M10 9h10M10 13h10M10 17h10M10 21h6" stroke="#222" stroke-width="1.3"/></svg>
    The Willowmere<br>Group Care
    <svg class="arr" viewBox="0 0 18 6"><path d="M0 3h16M13 1l3 2-3 2" fill="none" stroke="#222"/></svg>
  </div>
  <div class="node" style="left:471px;top:106px">
    <svg class="icon" viewBox="0 0 30 30"><rect x="6" y="3" width="18" height="24" rx="1" fill="none" stroke="#222" stroke-width="1.5"/><path d="M10 9h10M10 13h10M10 17h10M10 21h6" stroke="#222" stroke-width="1.3"/></svg>
    The Willowmere<br>Group Order
    <svg class="arr" viewBox="0 0 18 6"><path d="M0 3h16M13 1l3 2-3 2" fill="none" stroke="#222"/></svg>
  </div>
  <div class="hub">Willowmere</div>
  <div class="node" style="left:115px;top:323px">
    <svg class="icon" viewBox="0 0 30 30"><path d="M3 27h24" stroke="#222" stroke-width="1.5"/><path d="M7 26V18M12 26V14M17 26V16M22 26V8" stroke="#222" stroke-width="3"/><path d="M5 16l6-5 5 3 9-9" fill="none" stroke="#222"/></svg>
    Improved patient<br>outcome
    <svg class="arr" viewBox="0 0 18 6"><path d="M0 3h16M13 1l3 2-3 2" fill="none" stroke="#222"/></svg>
  </div>
  <div class="node" style="left:293px;top:323px">
    <svg class="icon" viewBox="0 0 30 30"><path d="M3 27h24" stroke="#222" stroke-width="1.5"/><path d="M7 26V18M12 26V14M17 26V16M22 26V8" stroke="#222" stroke-width="3"/><path d="M5 16l6-5 5 3 9-9" fill="none" stroke="#222"/></svg>
    Care<br>Standardization
    <svg class="arr" viewBox="0 0 18 6"><path d="M0 3h16M13 1l3 2-3 2" fill="none" stroke="#222"/></svg>
  </div>
  <div class="node" style="left:471px;top:323px">
    <svg class="icon" viewBox="0 0 30 30"><path d="M3 27h24" stroke="#222" stroke-width="1.5"/><path d="M7 26V18M12 26V14M17 26V16M22 26V8" stroke="#222" stroke-width="3"/><path d="M5 16l6-5 5 3 9-9" fill="none" stroke="#222"/></svg>
    Cost<br>Reduction
    <svg class="arr" viewBox="0 0 18 6"><path d="M0 3h16M13 1l3 2-3 2" fill="none" stroke="#222"/></svg>
  </div>
  <div class="pill" style="left:160px;top:472px;width:407px"><b>MEASURABLE OUTCOMES&nbsp;</b>WITH THE WILLOWMERE GROUP SOLUTIONS</div>

  <div class="label">The Willowmere Group Health Toolbox</div>
  <div class="rule"></div>
  <h2>Empowering Healthcare<br>Professionals</h2>
  <p>Lorem ipsum dolor sit amet, consectetur adipiscing elit, sed do eiusmod tempor incididunt ut labore et dolore magna aliqua. Quis ipsum suspendisse ultrices gravida. Risus commodo viverra maecenas accumsan lacus vel facilisis.</p>
  <div class="btn btn-white">Explore Solutions in Practice <svg viewBox="0 0 30 8"><path d="M0 4h28M24 1l4 3-4 3" fill="none" stroke="#222" stroke-width="1"/></svg></div>
</section>

<section class="find">
  <div class="panel"></div>
  <div class="label">Find a Solution</div>
  <div class="rule"></div>
  <h2>How can we help with your clinical<br>decision support needs?</h2>
  <p>Lorem ipsum dolor sit amet, consectetur adipiscing elit, sed do eiusmod tempor incididunt ut labore et dolore magna aliqua. Quis ipsum suspendisse ultrices gravida. Risus commodo viverra maecenas accumsan lacus vel facilisis.</p>
  <div class="opt" style="left:111px;top:268px"><i></i>Order Sets</div>
  <div class="opt" style="left:316px;top:268px"><i></i>Care Plans</div>
  <div class="opt" style="left:111px;top:313px"><i></i>Updates and Check-ups</div>
  <div class="opt" style="left:316px;top:313px"><i></i>Analytics</div>
  <div class="opt" style="left:111px;top:356px"><i></i>Care Standardization</div>
  <div class="opt" style="left:316px;top:356px"><i></i>Care Management</div>
  <div class="btn btn-brown">See Results <svg viewBox="0 0 30 8"><path d="M0 4h28M24 1l4 3-4 3" fill="none" stroke="#fff" stroke-width="1"/></svg></div>
  <div class="photo" role="img" aria-label="Circular photo of a doctor in scrubs talking with a patient" style="left:616px;top:53px;width:382px;height:382px;border-radius:50%;background:radial-gradient(circle at 55% 40%,#b8c9d6,#6f8ea8 55%,#3d4c57)"></div>
</section>

<div class="photo case-photo" role="img" aria-label="Photo of a therapist comforting a young woman seated in a chair"></div>
<section class="case">
  <div class="label">Case Studies</div>
  <div class="count">01 of 06</div>
  <div class="circ-btn" style="left:568px"><svg width="8" height="10" viewBox="0 0 8 10"><path d="M6 1L2 5l4 4" fill="none" stroke="#fff" stroke-width="1.3"/></svg></div>
  <div class="circ-btn" style="left:626px"><svg width="8" height="10" viewBox="0 0 8 10"><path d="M2 1l4 4-4 4" fill="none" stroke="#fff" stroke-width="1.3"/></svg></div>
  <h2>Maya's Journey: Overcoming Anxiety</h2>
  <p>Maya struggled with severe anxiety for years, making it difficult for her to participate in daily activities and maintain relationships. Through therapy and the support of her loved ones, she embarked on a journey of self-discovery and healing. This case study highlights the importance of early intervention, personalized treatment plans, and the positive impact of a strong support system in managing and overcoming anxiety disorders.</p>
  <div class="btn btn-white">Learn More <svg viewBox="0 0 30 8"><path d="M0 4h28M24 1l4 3-4 3" fill="none" stroke="#222" stroke-width="1"/></svg></div>
</section>

<section class="about">
  <div class="label">About The Willowmere Group</div>
  <div class="rule"></div>
  <h2>What We Believe</h2>
  <p>Lorem ipsum dolor sit amet, consectetur adipiscing elit. Vestibulum posuere elementum purus ut hendrerit. Vestibulum in leo rutrum, suscipit massa sit amet, placerat metus. Nam vulputate eleifend maximus. Duis auctor, lorem sed faucibus ornare, felis diam blandit arcu, feugiat consequat nisi libero dictum nibh. Nullam dapibus fringilla lacus.</p>
  <div class="btn btn-brown">More About Us <svg viewBox="0 0 30 8"><path d="M0 4h28M24 1l4 3-4 3" fill="none" stroke="#fff" stroke-width="1"/></svg></div>
  <div class="photo" role="img" aria-label="Circular photo of a counsellor taking notes beside a client lying on a sofa" style="left:676px;top:63px;width:412px;height:412px;border-radius:50%;background:radial-gradient(circle at 50% 45%,#c9d3dc,#8a9bad 55%,#4d5866)"></div>
</section>

<section class="insight ins-a">
  <div class="photo" role="img" aria-label="Illustration of a glowing blue digital brain" style="left:0;top:0;width:599px;height:341px;background:radial-gradient(circle at 50% 50%,#3a6a8c,#152838 60%,#0a1420)"></div>
  <div class="label" style="left:619px;top:50px">Insights</div>
  <div class="rule" style="left:619px;top:72px;width:469px;background:#777"></div>
  <h2 style="left:619px;top:84px">Understanding the Impact: Insights on<br>Mental Health Statistics</h2>
  <p style="left:619px;top:164px;color:#ddd">Explore our comprehensive collection of insights on mental health statistics. Gain a deeper understanding of the prevalence and impact of mental health conditions worldwide. Discover data on different demographics, age groups, and socioeconomic factors, shedding light on the challenges individuals face in their mental health journeys.</p>
  <div class="link-arrow" style="left:619px;top:277px">Read the Article <svg viewBox="0 0 30 8"><path d="M0 4h28M24 1l4 3-4 3" fill="none" stroke="#fff" stroke-width="1"/></svg></div>
</section>

<section class="insight ins-b">
  <div class="label" style="left:111px;top:50px">Insights</div>
  <div class="rule" style="left:111px;top:72px;width:459px;background:#c9b6a6"></div>
  <h2 style="left:111px;top:84px">Unraveling the Intricacies of Mental Health</h2>
  <p style="left:111px;top:130px;color:#f1e8e0">Explore our comprehensive collection of insights on mental health statistics. Gain a deeper understanding of the prevalence and impact of mental health conditions worldwide. Discover data on different demographics, age groups, and socioeconomic factors, shedding light on the challenges individuals face in their mental health journeys.</p>
  <div class="link-arrow" style="left:111px;top:277px">Read the Article <svg viewBox="0 0 30 8"><path d="M0 4h28M24 1l4 3-4 3" fill="none" stroke="#fff" stroke-width="1"/></svg></div>
  <div class="photo" role="img" aria-label="Digital illustration of a DNA helix beside a glowing blue head in profile" style="left:599px;top:0;width:601px;height:341px;background:linear-gradient(110deg,#0b1f4a,#1f4fa0 40%,#d89a4a 55%,#1c58b8 75%,#0a1a3e)"></div>
</section>

<section class="newsletter">
  <h2>Subscribe to Our Client Newsletter</h2>
  <p>Exclusively for The Willowmere Group clients, our quarterly newsletter highlights important practice changes, new topics and conditions, product innovations, and more.</p>
  <div class="email">
    <span>Enter Your Email*</span>
    <div class="btn btn-brown">Submit <svg viewBox="0 0 30 8"><path d="M0 4h28M24 1l4 3-4 3" fill="none" stroke="#fff" stroke-width="1"/></svg></div>
  </div>
</section>

<footer class="site-footer">
  <div class="logo">Willowmere Group</div>
  <div class="foot-links"><span>PRIVACY NOTICE</span><span>INTEREST-BASED ADS</span><span>TRADEMARKS</span><span>TERMS OF USE</span></div>
  <div class="social" style="left:957px"></div>
  <div class="social" style="left:1007px"></div>
  <div class="social" style="left:1057px"></div>
  <div class="rule"></div>
  <div class="copy" style="left:111px">© 2023 The Willowmere Group, Inc.</div>
  <div class="copy" style="left:925px">Privacy Policy</div>
  <div class="copy" style="left:1019px">Tearms of Use</div>
</footer>

</body>
</html>
```